Birch & Ember Website Design (Rustic/Western)

OVERVIEW
Birch & Ember Supply House (aka Birch & Ember) manufactures rustic / western furniture and décor for cabins, lodges, and ranches. We also offer a line of accessories to complement our product line.
WEB PAGE (www.BirchAndEmber.example)
We are looking for a new web page design to represent our mountain-style (log furniture) and country-style (barnwood furniture) product line. We would like to re-create our existing homepage with a similar style template for our product line.
Our website is currently under construction – a draft has been published as an example outline. We are currently using Plinkora.example for our online store.
THEME
The overall theme needs to appear rustic, yet elegant. Listed below are only suggestions, not requirements. Please use your own creativity.
* Photographs: We will use our own photographs, for now any photograph will suffice.
* Background Colors: dark brown (rgb 21-9-2), medium brown (rgb 39-17-4), light brown (rgb 72-34-3). White background is also an option.
* Font Colors: beige (rgb 233-164-118), gold (rgb 151-98-2)
• Mountain-Style Images: cabin, wildlife, mountains, fishing, wildlife, trees, etc.
* Mountain-Style Colors: hunter green
* Country-Style Images: western, ranch, barn, farm animals, horse buggies, horseshoes, etc.
* Country-Style Colors: maroon
Thanks to all who are participating.
Target Market(s)
Outdoor enthusiasts who enjoy mountain living or country living. Our primary target market is our local market and within a 100 mile radius of our location.
Industry/Entity Type
Construction
Requirements
Must have
- Rustic, yet elegant design.
Homepage and product template page for displaying each item.
Nice to have
- Source code and functionality is optional.
Mountain-Style theme to represent our collection of log furniture and décor suited for cabins and lodges. Suggested color: hunter green. Images may include cabin, wildlife, mountains, fishing, wildlife, trees, etc.
Country-Style theme to represent our collection of barnwood furniture and décor suited for farms and ranches. Suggested color: maroon. Images may include western, ranch, barn, farm animals, horse buggies, horseshoes, etc.

```html
<!DOCTYPE html>
<html lang="en">
<head>
<meta charset="utf-8">
<title>Birch &amp; Ember Supply House</title>
<link rel="stylesheet" href="https://fonts.googleapis.com/css2?family=Oxygen:wght@400;700&family=Oswald:wght@500;600&display=swap">
<style>
:root{
  --bg-dark:#271104;
  --bg-mid:#3a1a06;
  --bg-light:#482203;
  --accent:#d8782c;
  --beige:#e9a476;
  --gold:#c97a2a;
  --text-light:#f1d9c5;
  --hunter:#0f4a22;
  --maroon:#5e0a1c;
  --white:#ffffff;
}
*{margin:0;padding:0;box-sizing:border-box}
html,body{width:790px;height:1200px;overflow:hidden}
body{background:var(--bg-dark);font-family:"Oxygen",Arial,sans-serif;color:var(--beige);position:relative}
.top-rule{position:absolute;left:0;top:0;width:790px;height:3px;background:var(--accent)}
.brand{position:absolute;left:66px;top:14px;width:136px;height:84px;display:flex;flex-direction:column;align-items:center;border-bottom:3px solid var(--accent)}
.brand-mark{width:44px;height:44px;border-radius:50%;background:var(--bg-light);border:3px solid var(--accent);margin-top:4px}
.brand-name{margin-top:6px;font-size:11px;font-weight:700;color:var(--white);letter-spacing:1px;text-align:center;line-height:12px}
.search{position:absolute;left:590px;top:48px;width:135px;height:26px;background:var(--white);display:flex;align-items:center;justify-content:space-between;padding:0 6px}
.search span{font-size:8px;color:#333}
.main-nav{position:absolute;left:66px;top:108px;width:659px;height:45px;display:flex;background:linear-gradient(#6a3306,#3c1b04)}
.main-nav a{display:flex;align-items:center;justify-content:center;color:var(--beige);font-size:9.5px;text-decoration:none;border-right:1px solid #2a1204}
.main-nav a:last-child{border-right:none}
.hero{position:absolute;left:66px;top:153px;width:659px;height:275px;background:linear-gradient(#c9d3d9 0%,#9fb1bf 25%,#4f6f91 48%,#2f5778 62%,#3f6a55 80%,#2f5a3a 100%)}
.hero-title{position:absolute;left:58px;top:112px;font-family:"Oswald",sans-serif;font-weight:500;font-size:29px;color:#2a1a0e;letter-spacing:-0.5px}
.hero-arrow{position:absolute;top:119px;width:20px;height:20px;border-radius:50%;background:var(--white)}
.hero-dots{position:absolute;left:296px;top:253px;display:flex;gap:5px}
.hero-dots i{width:7px;height:7px;border-radius:50%;background:var(--white);display:block}
.hero-dots i:first-child{background:var(--accent)}
.welcome{position:absolute;left:66px;top:449px;width:377px}
.welcome h1{font-weight:400;font-size:16.5px;color:var(--accent);margin-bottom:8px}
.welcome p{font-size:9.4px;line-height:19.8px;color:var(--beige);text-align:justify}
.welcome-photo{position:absolute;left:456px;top:447px;width:269px;height:171px;background:linear-gradient(#8fb3d9 0%,#b9cfe0 38%,#9fa7a0 40%,#5e8a3c 50%,#4c7a30 100%)}
.promo{position:absolute;left:66px;top:650px;width:659px;height:59px;background:var(--bg-light);display:flex;align-items:center;justify-content:space-between;padding:0 23px 0 16px}
.promo h2{font-weight:400;font-size:20.5px;color:var(--accent)}
.promo a{width:160px;height:39px;background:var(--accent);color:#3a1a06;font-size:12px;font-weight:700;display:flex;align-items:center;justify-content:center;text-decoration:none;border-radius:2px}
.collection{position:absolute;top:735px;width:320px;height:215px}
.collection .photo{height:184px}
.collection .label{height:31px;display:flex;align-items:center;padding-left:9px;font-size:12.5px}
.mountain{left:66px}
.mountain .photo{background:linear-gradient(135deg,#b9782f,#8a4f1c 60%,#6e8e3c)}
.mountain .label{background:var(--hunter);color:#d9c29a}
.country{left:405px}
.country .photo{background:linear-gradient(#9fbfe0 0%,#c3d6e8 45%,#a8703f 60%,#5f8a3a 100%)}
.country .label{background:var(--maroon);color:#e6a07a}
.tile{position:absolute;top:974px;height:114px;border-radius:4px;display:flex;align-items:center;justify-content:center;font-family:"Oswald",sans-serif;font-weight:600;font-size:18px;color:var(--white)}
.tile-stores{left:66px;width:208px;background:linear-gradient(135deg,#5a5148,#8c7250)}
.tile-furniture{left:290px;width:210px;background:linear-gradient(90deg,#3f4a33,#8a5a2c 50%,#5c4a3a)}
.tile-decor{left:514px;width:211px;background:linear-gradient(135deg,#7a5230,#4f5a3a)}
.footer-links{position:absolute;left:66px;top:1122px;font-size:11.5px;color:var(--white);display:flex;gap:5px}
.footer-links a{color:var(--white);text-decoration:none}
.copyright{position:absolute;left:66px;top:1146px;font-size:8px;color:var(--white)}
.social{position:absolute;left:658px;top:1129px;display:flex;gap:5px}
.social span{width:19px;height:19px;border-radius:3px;background:#5a7fc0}
</style>
</head>
<body>
<div class="top-rule"></div>

<div class="brand">
  <div class="brand-mark"></div>
  <div class="brand-name">BIRCH &amp; EMBER</div>
</div>

<div class="search"><span>Search</span>
  <svg width="10" height="10" viewBox="0 0 10 10"><circle cx="4" cy="4" r="3" fill="none" stroke="#222" stroke-width="1.3"/><line x1="6.2" y1="6.2" x2="9" y2="9" stroke="#222" stroke-width="1.4"/></svg>
</div>

<nav class="main-nav">
  <a style="width:90px">Home</a>
  <a style="width:80px">Furniture</a>
  <a style="width:93px">Lighting</a>
  <a style="width:86px">Wall Decor</a>
  <a style="width:112px">Accessories</a>
  <a style="width:69px">Bargins</a>
  <a style="width:129px">Company</a>
</nav>

<section class="hero" role="img" aria-label="Snow-capped mountain range under a cloudy sky">
  <div class="hero-title">BIRCH &amp; EMBER</div>
  <svg class="hero-arrow" style="left:18px" viewBox="0 0 20 20"><circle cx="10" cy="10" r="10" fill="#fff"/><polyline points="11.5,6 7.5,10 11.5,14" fill="none" stroke="#333" stroke-width="2"/></svg>
  <svg class="hero-arrow" style="left:604px" viewBox="0 0 20 20"><circle cx="10" cy="10" r="10" fill="#fff"/><polyline points="8.5,6 12.5,10 8.5,14" fill="none" stroke="#333" stroke-width="2"/></svg>
  <div class="hero-dots"><i></i><i></i><i></i></div>
</section>

<section class="welcome">
  <h1>Welcome To Birch &amp; Ember</h1>
  <p>Lorem ipsum dolor sit amet, consectetuer adipiscing elit, sed diam nonummy nibh euismod tincidunt ut laoreet dolore magna aliquam erat volutpat. Ut wisi enim ad minim veniam, quis nostrud exerci tation ullamcorper suscipit lobortis nisl ut aliquip ex ea commodo consequat.Lorem ipsum dolor sit amet, consectetuer adipiscing elit, sed diam nonummy nibh euismod tincidunt ut laoreet dolore magna aliquam erat volutpat. Ut wisi enim ad minim veniam, quis nostrud exerci tation ullamcorper suscipit lobortis nisl ut aliquip ex ea commodo consequat.</p>
</section>
<div class="welcome-photo" role="img" aria-label="Log benches standing in a green meadow under a blue sky"></div>

<section class="promo">
  <h2>Rustic / Western Furniture &amp; Accessories</h2>
  <a>Online Shoping</a>
</section>

<div class="collection mountain">
  <div class="photo" role="img" aria-label="Cedar-panelled cabin bathroom with a tub and window"></div>
  <div class="label">Mountain-Style Collection</div>
</div>
<div class="collection country">
  <div class="photo" role="img" aria-label="Cattle grazing in a green pasture under a blue sky"></div>
  <div class="label">Country-Style Collection</div>
</div>

<div class="tile tile-stores" role="img" aria-label="Wooden planter boxes with red flowers">ONLINE STORES</div>
<div class="tile tile-furniture" role="img" aria-label="Rustic wooden shelf outdoors">FURNITURE</div>
<div class="tile tile-decor" role="img" aria-label="Wooden wall sign with pine trees">WALL DECORS</div>

<nav class="footer-links">
  <a>Home</a><span>|</span><a>About Us</a><span>|</span><a>Email</a><span>|</span><a>Store</a><span>|</span><a>Contact Us</a><span>|</span><a>Blog</a>
</nav>
<div class="copyright">© 2014 Company Name &nbsp;All right reserved &nbsp;Term of Use</div>
<div class="social"><span></span><span style="background:#5bb5e6"></span><span style="background:#8a6a52"></span></div>
</body>
</html>
```